BrightFern Life Insurance Web Design Project

We need a beautiful and simple website design to better explain our life insurance business, products and why people need life insurance.
We want the site to stand out as being simple and compelling.
As we are an old "friendly society" that has been in Australia for 130 years, we want to stand for trust, simplicity, but also longevity and security (we are supported by a global reinsurer)
We will allow customers to directly get a quote and apply for life insurance through the website.
We want a very modern look, with our exisiting gold and dark blue colours.
Target Market(s)
30-50 YOs
Industry/Entity Type
Life Insurance
Requirements
Must have
- - Life insurance quick quotation tool.
- Phone number.
- Ability to drill to information on different types of life insurance.
- Positive imagery
- our logo (refer www.brightfern-example.com.au)
Nice to have
- Target market is 30-40year olds.
Portal for advisers to access
Should not have
- Clip art
Cliched images

```html
<!DOCTYPE html>
<html lang="en">
<head>
<meta charset="utf-8">
<title>BrightFern Life Insurance</title>
<link rel="stylesheet" href="https://fonts.googleapis.com/css2?family=Noto+Sans:wght@400;700&display=swap">
<style>
:root{
  --gold:#c9a83a;
  --gold-dark:#a98a25;
  --gold-band:#cdad3c;
  --navy:#2b2a86;
  --text:#5e5e5e;
  --text-dark:#444;
  --panel:#efeef4;
  --nav-bg:#efeff3;
  --line:#dcdce2;
  --white:#fff;
}
*{box-sizing:border-box;margin:0;padding:0}
html,body{width:819px;height:1200px;overflow:hidden;background:var(--white)}
body{position:relative;font-family:"Noto Sans",Verdana,sans-serif;color:var(--text)}
.abs{position:absolute}

.brand{left:102px;top:50px;display:flex;align-items:center;gap:8px}
.brand-mark{width:14px;height:14px;background:var(--navy)}
.brand-name{font-size:22px;color:var(--navy);font-weight:400;letter-spacing:.2px}

.btn{background:var(--gold);color:var(--white);text-align:center;border:2px solid #e9dcae;box-shadow:0 1px 2px rgba(0,0,0,.25);text-decoration:none;display:block}
.btn-top{top:64px;height:33px;line-height:29px;font-size:13.5px}
.btn-quote{left:464px;width:120px}
.btn-portal{left:594px;width:140px}

.main-nav{left:86px;top:110px;width:648px;height:42px;background:var(--nav-bg);border:2px solid var(--line);display:flex;align-items:center;font-size:11px}
.main-nav a{color:var(--text);text-decoration:none;position:absolute}
.main-nav a.active{color:var(--gold-dark)}

.hero{left:88px;top:164px;width:645px;height:378px;border:3px solid var(--white);box-shadow:0 0 4px rgba(0,0,0,.25);
  background:linear-gradient(100deg,#6f7760 0%,#b8b1a0 18%,#e9e5dc 40%,#c9b39a 55%,#8a6f57 70%,#4a6aa0 88%,#d8dbd6 100%)}
.slider-dots{left:390px;top:553px;display:flex;gap:6px}
.slider-dots span{width:11px;height:11px;border-radius:50%;background:#a0a0a4}
.slider-dots span.on{background:var(--gold)}

.content-panel{left:90px;top:632px;width:641px;height:498px;background:var(--panel);box-shadow:0 0 4px rgba(0,0,0,.25)}

.products{left:117px;top:590px;width:589px;height:252px;background:var(--gold-band);box-shadow:0 2px 4px rgba(0,0,0,.35)}
.product{position:absolute;top:0;height:252px;text-align:center;color:var(--white)}
.product + .product{border-left:1px dashed #efe1a6}
.product .icon{width:48px;height:48px;border-radius:50%;border:2px solid #f1ead0;margin:16px auto 0;
  background:radial-gradient(circle at 45% 45%,#e9d2bf,#8a6a52 60%,#3b3330)}
.product h3{font-weight:400;font-size:12px;line-height:14px;margin-top:12px}
.product p{font-size:10.3px;line-height:14.4px;text-align:justify;text-align-last:left;color:#fbf4dc;margin:12px 11px 0 13px;letter-spacing:.2px}
.btn-read{position:absolute;top:222px;height:21px;line-height:19px;font-size:10.5px;width:76px;background:#b89a2c;border:1px solid #9c801f;color:var(--white);box-shadow:0 1px 2px rgba(0,0,0,.3)}

.welcome{left:123px;top:864px;width:351px}
.section-title{font-size:17px;font-weight:400;color:var(--text-dark);margin-bottom:8px}
.welcome p{font-size:11.6px;line-height:20px;text-align:justify;letter-spacing:.3px}
.btn-more{left:124px;top:1082px;width:55px;height:27px;line-height:23px;font-size:13px}

.finder{left:502px;top:864px;width:200px}
.finder p{font-size:11.6px;line-height:20px;text-align:justify;letter-spacing:.3px}
.field{position:absolute;left:505px;width:195px;height:27px;background:var(--white);border:1px solid #d4d4d8;box-shadow:inset 0 1px 2px rgba(0,0,0,.12);font-size:10.5px;line-height:25px;padding-left:8px;color:var(--text)}
.btn-submit{left:506px;top:1048px;width:70px;height:27px;line-height:23px;font-size:13px}
.call-line{left:505px;top:1090px;font-size:11.6px;color:var(--text);text-decoration:underline}

.site-footer{left:0;top:1147px;width:819px;text-align:center;font-size:10px;line-height:15px;color:var(--text-dark)}
.site-footer em{text-decoration:underline}
</style>
</head>
<body>
<header>
  <div class="abs brand"><span class="brand-mark"></span><span class="brand-name">BrightFern</span></div>
  <a class="abs btn btn-top btn-quote" href="#">Free Quote</a>
  <a class="abs btn btn-top btn-portal" href="#">Adviser Portal</a>
  <nav class="abs main-nav">
    <a class="active" href="#" style="left:32px">Home</a>
    <a href="#" style="left:104px">About Us</a>
    <a href="#" style="left:192px">Choosing Life Insurance</a>
    <a href="#" style="left:354px">Get Life Insurance</a>
    <a href="#" style="left:490px">Claims</a>
    <a href="#" style="left:558px">Contact Us</a>
  </nav>
</header>

<div class="abs hero" role="img" aria-label="Photo of an adviser talking with a couple at a kitchen table"></div>
<div class="abs slider-dots"><span class="on"></span><span></span><span></span></div>

<div class="abs content-panel"></div>

<section class="abs products">
  <div class="product" style="left:0;width:115px">
    <div class="icon" role="img" aria-label="Photo of joined hands"></div>
    <h3>Life<br>Insurance</h3>
    <p>We will allow customers to directly get a quote and apply for life insurance through the website.</p>
    <a class="btn-read" href="#" style="left:14px">Read More</a>
  </div>
  <div class="product" style="left:115px;width:112px">
    <div class="icon" role="img" aria-label="Photo of a bandaged arm"></div>
    <h3>Disablement<br>Insurance</h3>
    <p>We will allow customers to directly get a quote and apply for life insurance through the website.</p>
    <a class="btn-read" href="#" style="left:10px">Read More</a>
  </div>
  <div class="product" style="left:227px;width:112px">
    <div class="icon" role="img" aria-label="Photo of a bandaged arm"></div>
    <h3>Trauma<br>Insurance</h3>
    <p>We will allow customers to directly get a quote and apply for life insurance through the website.</p>
    <a class="btn-read" href="#" style="left:11px">Read More</a>
  </div>
  <div class="product" style="left:339px;width:122px">
    <div class="icon" role="img" aria-label="Photo of a worker at her job"></div>
    <h3>Income Protection<br>Insurance</h3>
    <p>We will allow customers to directly get a quote and apply for life insurance through the website.</p>
    <a class="btn-read" href="#" style="left:17px">Read More</a>
  </div>
  <div class="product" style="left:461px;width:128px">
    <div class="icon" role="img" aria-label="Photo of a business person's folded hands"></div>
    <h3>Business Expenses<br>Insurance</h3>
    <p>We will allow customers to directly get a quote and apply for life insurance through the website.</p>
    <a class="btn-read" href="#" style="left:15px">Read More</a>
  </div>
</section>

<section class="abs welcome">
  <h2 class="section-title">Welcome to our site</h2>
  <p>As we are an old "friendly society" that has been in Australia for 130 years, we want to stand for trust, simplicity, but also longevity and security (we are supported by a global reinsurer).<br>We will allow customers to directly get a quote and apply for life insurance through the website. As we are an old "friendly society" that has been in Australia for 130 years, we want to stand for trust, simplicity, but also longevity and security (we are supported by a global reinsurer).</p>
</section>
<a class="abs btn btn-more" href="#">More</a>

<section class="abs finder">
  <h2 class="section-title">Find an advertiser</h2>
  <p>Find an advertiser to select a suitable sheme as per you.</p>
</section>
<div class="field" style="top:941px">Your Name</div>
<div class="field" style="top:977px">Mobile No</div>
<div class="field" style="top:1013px">Email Id</div>
<a class="abs btn btn-submit" href="#">Submit</a>
<a class="abs call-line" href="#">Call us now @ 1500 246 810</a>

<footer class="abs site-footer">Copyright @ 2012, <em>BrightFern</em><br>Terms &amp; Privacy Policy</footer>
</body>
</html>
```